Personal letterhead and stationary

I am looking for someone to design letterhead and stationary set for my personal use. I want something simple and timeless with a little bit of color. I like photography, computers and writing.

```html
<!DOCTYPE html>
<html lang="en">
<head>
<meta charset="utf-8">
<title>Marcus Holt — Personal Stationery</title>
<link rel="stylesheet" href="https://fonts.googleapis.com/css2?family=PT+Sans+Narrow:wght@400;700&display=swap">
<style>
  :root {
    --ink: #231f20;
    --slate: #646466;
    --red: #d41f3c;
    --paper: #ffffff;
    --backdrop: #ececee;
    --flap-grey: #cfcfcf;
    --rule-grey: #d4d4d6;
  }
  html, body {
    margin: 0;
    padding: 0;
    width: 1200px;
    height: 900px;
    overflow: hidden;
    background: var(--backdrop);
    font-family: "PT Sans Narrow", "Arial Narrow", sans-serif;
  }
  .canvas { position: relative; width: 1200px; height: 900px; }

  .wordmark {
    position: absolute;
    display: flex;
    align-items: center;
    gap: 10px;
    color: var(--ink);
    font-weight: 700;
    text-transform: uppercase;
    letter-spacing: 1px;
    line-height: 1;
    white-space: nowrap;
  }
  .wordmark-dot { background: var(--red); flex: none; }

  /* Letterhead */
  .letterhead {
    position: absolute;
    left: 80px; top: 92px;
    width: 532px; height: 689px;
    background: var(--paper);
  }
  .letterhead .wordmark { left: 55px; top: 22px; font-size: 40px; }
  .letterhead .wordmark-dot { width: 12px; height: 12px; }
  .letterhead-rule {
    position: absolute;
    left: 55px; top: 641px;
    width: 297px; height: 2px;
    background: var(--red);
  }
  .letterhead-contact {
    position: absolute;
    right: 55px; top: 634px;
    text-align: right;
    color: var(--ink);
    font-size: 11px;
    line-height: 14px;
  }
  .letterhead-contact .contact-name {
    color: var(--red);
    font-weight: 700;
    font-size: 13px;
    text-transform: uppercase;
    letter-spacing: 0.5px;
  }
  .letterhead-contact .gap { display: inline-block; width: 6px; }

  /* Card */
  .card {
    position: absolute;
    left: 637px; top: 176px;
    width: 540px; height: 261px;
    background: var(--paper);
  }
  .card-band {
    position: absolute; left: 0; top: 0;
    width: 100%; height: 24px;
    background: var(--red);
  }
  .card-band-edge {
    position: absolute; left: 0; top: 24px;
    width: 100%; height: 4px;
    background: var(--rule-grey);
  }
  .card .wordmark { left: 29px; top: 46px; font-size: 26px; }
  .card .wordmark-dot { width: 8px; height: 8px; }
  .card-footer {
    position: absolute;
    left: 29px; right: 33px; top: 238px;
    display: flex;
    align-items: center;
    gap: 12px;
    color: var(--ink);
    font-size: 11px;
    font-weight: 700;
    letter-spacing: 0.6px;
    white-space: nowrap;
  }
  .card-footer .divider {
    flex: 1;
    height: 2px;
    background: var(--red);
  }

  /* Envelope */
  .envelope {
    position: absolute;
    left: 637px; top: 480px;
    width: 539px; height: 250px;
    background: var(--paper);
  }
  .envelope-stripe {
    position: absolute; left: 8px; right: 6px; top: 53px;
    height: 9px;
    background: var(--red);
  }
  .envelope-gum {
    position: absolute; left: 10px; right: 8px; top: 62px;
    height: 33px;
    background: var(--flap-grey);
    border-radius: 0 0 8px 8px;
  }
</style>
</head>
<body>
<main class="canvas">

  <section class="letterhead" aria-label="Letterhead">
    <div class="wordmark">Marcus Holt <span class="wordmark-dot"></span></div>
    <div class="letterhead-rule"></div>
    <address class="letterhead-contact" style="font-style:normal">
      <div class="contact-name">Marcus Dean Holt.</div>
      <div>48 Alder Lane.<span class="gap"></span>Hartford, CT 06105.</div>
      <div>+1 800.555.0142.</div>
    </address>
  </section>

  <section class="card" aria-label="Note card">
    <div class="card-band"></div>
    <div class="card-band-edge"></div>
    <div class="wordmark">Marcus Holt <span class="wordmark-dot"></span></div>
    <div class="card-footer">
      <span>Marcus Dean Holt.</span>
      <span class="divider"></span>
      <span>Hartford, CT 06105.</span>
      <span class="divider"></span>
      <span>Alder Lane.</span>
    </div>
  </section>

  <section class="envelope" aria-label="Envelope">
    <div class="envelope-stripe"></div>
    <div class="envelope-gum"></div>
  </section>

</main>
</body>
</html>
```